KTV Consulting

Government/Entitlement Consulting Services- I assist developers obtain entitlements from local, state and federal government agencies so that they can build their projects. Often these projects are very complicated and political and may face community opposition.

Target Market(s)

Real Estate Developers

Industry/Entity Type

Business Consultant

Contact Information for Business Card

Dana Pelletier
Principal

Font styles to use
Serif
Sans Serif

Requirements
Must have
• Classy and professional appeal.
Nice to have
• I like a combination of a mat and glossy finish. I've seen that done with black and then a bold color for a pop, but am not 100% committed to that.

```html
<!DOCTYPE html>
<html lang="en">
<head>
<meta charset="utf-8">
<title>KTV Consulting – Business Card</title>
<link rel="stylesheet" href="https://fonts.googleapis.com/css2?family=Montserrat:wght@600&family=Open+Sans:wght@400;600&display=swap">
<style>
  :root {
    --backdrop: #3b3431;
    --card-black: #0d0d0d;
    --card-edge: #1c1c1c;
    --accent-blue: #4ba3e8;
    --silver: #cfcfcf;
    --text-white: #f1f1f1;
    --divider: #3a3a3a;
  }
  * { margin: 0; padding: 0; box-sizing: border-box; }
  html, body {
    width: 1200px;
    height: 900px;
    overflow: hidden;
    background: var(--backdrop);
  }
  .canvas {
    position: relative;
    width: 1200px;
    height: 900px;
    display: flex;
    align-items: center;
    justify-content: center;
    gap: 60px;
  }
  .card {
    position: relative;
    width: 510px;
    height: 292px;
    background: var(--card-black);
    border: 1px solid var(--card-edge);
    box-shadow: 0 12px 30px rgba(0,0,0,0.45);
  }

  /* Front: wordmark + contact details */
  .card-front .wordmark {
    position: absolute;
    left: 42px;
    top: 118px;
    width: 220px;
    font-family: "Montserrat", sans-serif;
    font-weight: 600;
    color: var(--accent-blue);
    line-height: 1;
  }
  .wordmark .mark-main {
    display: block;
    font-size: 52px;
    letter-spacing: 2px;
  }
  .wordmark .mark-sub {
    display: block;
    font-size: 23px;
    letter-spacing: 1.5px;
    margin-top: 6px;
  }
  .card-front .divider {
    position: absolute;
    left: 282px;
    top: 64px;
    width: 1px;
    height: 168px;
    background: var(--divider);
  }
  .contact {
    position: absolute;
    left: 300px;
    top: 64px;
    font-family: "Open Sans", sans-serif;
    color: var(--text-white);
    font-size: 12.5px;
    line-height: 1.35;
  }
  .contact .person-name {
    font-size: 15px;
    font-weight: 600;
    color: var(--accent-blue);
  }
  .contact .person-title { margin-bottom: 12px; }
  .contact .address { margin-bottom: 10px; }
  .contact-list { list-style: none; }
  .contact-list li {
    display: flex;
    align-items: center;
    gap: 8px;
  }
  .contact-list svg { width: 10px; height: 10px; fill: var(--accent-blue); flex: none; }

  /* Back: foil wordmark */
  .card-back .wordmark {
    position: absolute;
    left: 0;
    right: 0;
    top: 96px;
    text-align: center;
    font-family: "Montserrat", sans-serif;
    font-weight: 600;
    color: var(--silver);
    line-height: 1;
  }
</style>
</head>
<body>
<main class="canvas">
  <section class="card card-front" aria-label="Card front">
    <div class="wordmark">
      <span class="mark-main">KTV</span>
      <span class="mark-sub">CONSULTING</span>
    </div>
    <div class="divider"></div>
    <div class="contact">
      <p class="person-name">Dana Pelletier</p>
      <p class="person-title">Principal</p>
      <p class="address">2150 Harbor Street<br>Lakeview, IL 60614.</p>
      <ul class="contact-list">
        <li>
          <svg viewBox="0 0 10 10" aria-hidden="true"><path d="M2 0.5 L3.6 2.8 L2.7 3.8 Q3.8 6 6.2 7.3 L7.2 6.4 L9.5 8 L8.3 9.5 Q3.5 8.8 0.5 1.7 Z"/></svg>
          <span>044-555 016 248</span>
        </li>
        <li>
          <svg viewBox="0 0 10 10" aria-hidden="true"><path d="M0.5 2 H9.5 V8 H0.5 Z M1 2.4 L5 5.4 L9 2.4" stroke="#0d0d0d" stroke-width="0.8"/></svg>
          <span>info@ktvconsult.com</span>
        </li>
        <li>
          <svg viewBox="0 0 10 10" aria-hidden="true"><circle cx="5" cy="5" r="4.6"/><path d="M0.6 5 H9.4 M5 0.4 Q2 5 5 9.6 M5 0.4 Q8 5 5 9.6" stroke="#0d0d0d" stroke-width="0.7" fill="none"/></svg>
          <span>www.ktvconsult.com</span>
        </li>
      </ul>
    </div>
  </section>

  <section class="card card-back" aria-label="Card back">
    <div class="wordmark">
      <span class="mark-main">KTV</span>
      <span class="mark-sub">CONSULTING</span>
    </div>
  </section>
</main>
</body>
</html>
```